Meadowlark Lane Yoga Facebook Design

"Practice Radiant Movement"

Foundational and sustainable yoga practice to cultivate growth through a variety of anatomy- informed movement patterns. Develop an informative and inspirational connection with the mind, body and spirit, through smart and integrated movement.

-I need a design that is happy and cheerful and attracts children and adults alike. I teach vinyassa based yoga that is sustainable and smart, kid yoga, and chair yoga.

-A movement practic rooted in foundation, core, and expression

- Accessible yoga for a sustained practice. A guided movement practice where one gains information and knowledge of oneself through a mind/body connection. For one feel good physically with a new awareness of their internal radiance that exists in all beings. Physical rejuvenation egnites a light and increases energy to flow through the physical body, which ultimately tranlates into works of kindness for others and out in the world.

Nora Whitfield
Yoga Instructor
MD, Pediatrician
RYT-200
RCYT
Certified yoga teacher for adults and children

Full description:
What is the positioning or mission statement of your company? to guide individuals in a yoga-based safe and sustainable movement practice applicable to all ages and body types. Currently my focus is working with children in daycare and school settings, but my goal is to expand into private yoga practice for adults, and potentially as part of rented space in studios. I hope to find a way to work with children AND adults (so would love for logo to be appealing to both), but current focus is with children based on need and demand in the community. yoga for children also compliments my backround as a pediatrician/neonatologist, and I greatly miss interacting with children. I also want to emphasize a yoga/movement practice that is focused more on what one feels internally through movement. NOT what one looks like asthetically. I believe in removing all mirrors from yoga/movement practice. It should be an experience of movement/poses/yoga through appropriate cueing and education. It is not about the details of how far the knee should bend, or how high the leg should be. Focusing on foudation first, core, then core engagement and ultimately expression of poses/movements. A focus on strength, stability and mobility, not just flexibility, which is the common perception/association with yoga. I also want individuals to learn to be an advocate of their own health. Through guidance, I hope for individuals to connect with their body so they know themselves so well to be able to advocate for themselves in the modern healthcare world. This internal experience and connection is so essential in a world where modern medicine has become a business and it is all about making a dollar. the connection with patients is lost, and individuals need to learn to empower themselves and through their new found voice to be able to articulate what is wrong.
Does your company have a tagline or slogan that should be included with the logo? "Practice Radiant Movement"
What do you hope your company can be known for? Accessible yoga for a sustained practice. A guided movement practice where one gains information and knowledge of oneself through a mind/body connection. For one feel good physically with a new awareness of their internal radiance that exists in all beings. Physical rejuvenation egnites a light and increases energy to flow through the physical body, which ultimately tranlates into works of kindness for others and out in the world.
What color palettes might you prefer? why? love the colors currently chosen
Where will the logo be primarily used? initially business cards, but hopefully future websites, t-shirts, and potentially local magazine adds. Also starting with a small couple of banners for community events in the area. I currently practice as a nomad out of my car :)
Are there any elements you would prefer to see in the logo? Movement. A modern depiction of a human body/figure practicing movement. Hoping to avoid a stereotypical yoga pose per say, just because I want to people to think of it more of a movement practice with yoga roots. Modern yoga. There are elements of breathing and connecting with oneself through the flow of breath and movement, but I do not focus on the meditative/cerebral aspect of the yoga practice. What I teach is almost reaching a meditative state through movement. I personally don't practice, nor resonate with just seated meditation. just not my thing :)
In your opinion, what defines a well-designed logo? curiosity. enough info for individuals to think they know what it means, but want to know more. invokes curiosity, but not too abstract. Reproducible. not too complicated. I want also to invoke a community feel, so a design that appeals to all people within a community.
What is your preference in reference to icons, typography, spokespeople (characters), etc.? modern design. I love the idea of a logo for my purposes, to invoke a sense of movement from within. So not too static.
What words or icons must be included in the logo? movement with yoga roots.
What logos do you like and why? A representation, but not exact. I think some ambiguity is intriguing for others, and also memorable. I want it to be an artistic representation of movement/yoga
What logos do you dislike and why? too busy, too loud.
In your opinion, what is the primary purpose for a logo? association
Who is the primary target audience? (who is most likely to use your services/product?) Children and their parents, but ultimately to expand into teaching adults. I even have aspirations of prenatal and post-natal yoga. Potentially incorporating infants.
Who currently uses your product the most? n/a (working in schools/daycare currently. It is currently all volunteer)
Are you pleased with the range of people your company serves? n/a
Are you looking to expand, modify, or completely change your target audience? or will it remain the same? yes! expand into an adult audience.
How do you plan to focus on your target audience? currently by working through schools and daycares. hopefully ultimately through after school care programs and then offering kid yoga in an existing yoga studio (working on this with Q studio in Ridgeland, currently)
What are your main forms of advertising? word of mouth, schools, daycares. Happy kids talking to their parents about the yoga class they took and happy teachers :)
How do most customers find out about your company?
Which gender are you targeting? All genders! However, with kid yoga, often the maternal individual in the child's life is more involved with decision making as far as extracurricular activities

Target Market(s)

Adults, children and families interested in movement, wellness and fun

Font styles to use
Sans Serif

Requirements
Must have
• ***I meant to emphasize the that "S" figure in my logo is SOOO iimportant to me. My daughter designed it. please highlight the "S" figure if possible******
My logo and the phrase "practice radiant movement"
Same colors as my logo
Feel like movement and fun.
Attracts children and families
Incorporate pieces of my description somehow
Nice to have
• different yoga poses or figures in movement
abstract design
attacts all body types and genders
inclusive

Industry is yoga, movement, wellness
Should not have
• no darkness
want happy and vibrant, inviting

```html
<!DOCTYPE html>
<html lang="en">
<head>
<meta charset="utf-8">
<title>Meadowlark Lane Yoga – Practice Radiant Movement</title>
<link href="https://fonts.googleapis.com/css2?family=Saira+Extra+Condensed:wght@600;700&family=Mulish:wght@600;700;800&display=swap" rel="stylesheet">
<style>
  :root {
    --cream: #faf8e2;
    --lemon: #f3ee9c;
    --gold: #b8922c;
    --gold-light: #e0c25a;
    --gold-dark: #8a6a17;
    --rust: #7a2414;
    --teal: #2aa2ba;
    --sun: #f5cb1c;
    --ink: #1d1d1d;
    --sky-light: #c9f4fb;
    --sky: #7fd9ea;
  }
  * { margin: 0; padding: 0; box-sizing: border-box; }
  html, body { width: 800px; height: 1200px; overflow: hidden; background: var(--cream); }
  .poster {
    position: relative;
    width: 800px;
    height: 1200px;
    overflow: hidden;
    background: linear-gradient(180deg, var(--cream) 0%, #f7f4c8 55%, var(--lemon) 100%);
    font-family: "Mulish", sans-serif;
    text-align: center;
  }
  .poster-frame {
    position: absolute;
    inset: 7px;
    border: 3px solid var(--gold);
    pointer-events: none;
  }
  .display-type {
    position: absolute;
    left: 0; top: 0;
    width: 800px; height: 1200px;
    pointer-events: none;
  }
  .display-type text {
    font-family: "Saira Extra Condensed", sans-serif;
    font-weight: 700;
  }
  .tagline-lead { fill: var(--gold); font-size: 86px; }
  .tagline-main { fill: url(#goldFill); font-size: 166px; }
  .instructor-name { fill: var(--rust); font-size: 98px; }
  .portrait {
    position: absolute;
    left: 267px;
    top: 261px;
    width: 232px;
    height: 232px;
    border-radius: 50%;
    background: radial-gradient(circle at 50% 45%, var(--sky-light) 0%, var(--sky) 70%, #5ec6dc 100%);
    box-shadow: 0 0 18px 6px rgba(255, 255, 255, 0.85);
  }
  .info-line {
    position: absolute;
    left: 0; right: 0;
    line-height: 1;
    white-space: nowrap;
  }
  .role {
    top: 602px;
    font-size: 42px;
    font-weight: 800;
    letter-spacing: 1px;
    color: var(--teal);
  }
  .degree {
    top: 650px;
    font-size: 24px;
    font-weight: 700;
    color: var(--gold);
  }
  .credentials {
    top: 688px;
    font-size: 40px;
    font-weight: 800;
    color: var(--rust);
  }
  .summary {
    top: 741px;
    font-size: 42px;
    font-weight: 700;
    line-height: 1.1;
    color: var(--rust);
  }
  .brand {
    position: absolute;
    left: 0; right: 0;
    top: 955px;
    display: flex;
    align-items: center;
    justify-content: center;
    gap: 16px;
  }
  .brand-dot {
    width: 64px;
    height: 64px;
    border-radius: 50%;
    background: var(--sun);
  }
  .brand-name {
    font-size: 34px;
    font-weight: 700;
    color: var(--teal);
    white-space: nowrap;
  }
  .phone {
    top: 1105px;
    font-size: 44px;
    font-weight: 800;
    letter-spacing: 1px;
    color: var(--gold);
  }
  .email {
    top: 1147px;
    font-size: 24px;
    font-weight: 600;
    color: var(--ink);
  }
</style>
</head>
<body>
  <main class="poster">
    <div class="poster-frame"></div>

    <div class="portrait" role="img" aria-label="Portrait photo of the instructor with hands in prayer position against a light blue background"></div>

    <svg class="display-type" viewBox="0 0 800 1200" aria-hidden="false">
      <defs>
        <linearGradient id="goldFill" x1="0" y1="0" x2="0" y2="1">
          <stop offset="0" stop-color="#e0c25a"/>
          <stop offset="0.5" stop-color="#b8922c"/>
          <stop offset="1" stop-color="#8a6a17"/>
        </linearGradient>
        <filter id="softShadow" x="-5%" y="-5%" width="110%" height="120%">
          <feDropShadow dx="2" dy="3" stdDeviation="2" flood-color="#78591a" flood-opacity="0.35"/>
        </filter>
      </defs>
      <text class="tagline-lead" x="178" y="99" textLength="429" lengthAdjust="spacingAndGlyphs">PRACTICE RADIANT</text>
      <text class="tagline-main" x="147" y="236" textLength="506" lengthAdjust="spacingAndGlyphs" filter="url(#softShadow)">MOVEMENT</text>
      <text class="instructor-name" x="160" y="596" textLength="479" lengthAdjust="spacingAndGlyphs">NORA WHITFIELD</text>
    </svg>

    <p class="info-line role">YOGA INSTRUCTOR</p>
    <p class="info-line degree">(MD, Pediatrician)</p>
    <p class="info-line credentials">RYT-200,RCYT</p>
    <p class="info-line summary">Certified yoga teacher for<br>adults and children</p>

    <div class="brand">
      <span class="brand-dot"></span>
      <span class="brand-name">Meadowlark Lane Yoga</span>
    </div>

    <p class="info-line phone">555-014-2286</p>
    <p class="info-line email">norawhitfield@example.com</p>
  </main>
</body>
</html>
```